Signboard menu for a Fastfood takeaway shop

My current signboard menu is old now, I want to upgrade to a new, bigger and brighter signboard menu.
Photos of the old menu attached but there are some changes in each sections of the menu needs to be changed.
Size of the signboard :
L: 1700cm
H: 1200cm

Industry/Entity Type

Fastfood Hospitality

Colors
FFC000
F8CF3A
FAE287
FDF2CF
FEFAEE

```html
<!DOCTYPE html>
<html lang="en">
<head>
<meta charset="utf-8">
<title>Takeaway Menu Board</title>
<link href="https://fonts.googleapis.com/css2?family=Montserrat:wght@500;600;800&family=Josefin+Sans:wght@600;700&display=swap" rel="stylesheet">
<style>
  :root{
    --page:#d9d9d9;
    --board-edge:#c92a2d;
    --board-mid:#ef5052;
    --heading:#cdd629;
    --item:#f6ecec;
    --price:#f2d33c;
    --rule:#f3dede;
    --art:rgba(255,255,255,0.22);
  }
  *{box-sizing:border-box;margin:0;padding:0}
  html,body{width:1200px;height:1000px;overflow:hidden;background:var(--page)}
  .board{
    position:absolute;left:15px;top:118px;width:1170px;height:764px;overflow:hidden;
    background:radial-gradient(ellipse at 55% 45%,var(--board-mid) 0%,#e0403f 55%,var(--board-edge) 100%);
    box-shadow:0 10px 24px rgba(0,0,0,.35);
    font-family:"Josefin Sans",sans-serif;color:var(--item);
  }
  .section{position:absolute}
  .section h2{
    font-family:"Montserrat",sans-serif;font-weight:800;font-size:18px;
    color:var(--heading);letter-spacing:1px;line-height:1;white-space:nowrap;
  }
  .section h2.tight{font-size:17px;letter-spacing:-0.6px}
  .rule{height:2px;background:var(--rule);margin:5px 0 9px}
  .grid{display:grid;grid-template-columns:1fr 1fr;column-gap:14px}
  .grid .full{grid-column:1 / span 2}
  .row{
    display:flex;align-items:baseline;font-size:8.6px;font-weight:700;
    letter-spacing:1.6px;text-transform:uppercase;height:17.6px;white-space:nowrap;
  }
  .row .dots{flex:1;border-bottom:1px dotted var(--item);margin:0 4px;transform:translateY(-2px);min-width:10px}
  .row .price{color:var(--price);font-family:"Montserrat",sans-serif;font-weight:600;font-size:9.5px;letter-spacing:.5px}
  .text{font-size:8.6px;font-weight:700;letter-spacing:1.6px;text-transform:uppercase;line-height:17px}
  .note{color:var(--price)}
  .pack{margin-bottom:12px}
  .art{position:absolute;background:var(--art);border-radius:10px}
</style>
</head>
<body>
<div class="board">

  <!-- Left column -->
  <section class="section" style="left:16px;top:40px;width:372px">
    <h2>SANDWICHES:</h2>
    <div class="rule" style="width:226px"></div>
    <div class="grid" style="grid-template-columns:172px 186px">
      <div class="row"><span>Yeast Spread</span><span class="dots"></span><span class="price">$ 4.50</span></div>
      <div class="row"><span>Rissole</span><span class="dots"></span><span class="price">$ 7.50</span></div>
      <div class="row"><span>Cheese</span><span class="dots"></span><span class="price">$ 4.50</span></div>
      <div class="row"><span>Sausage</span><span class="dots"></span><span class="price">$ 7.00</span></div>
      <div class="row"><span>Tomato</span><span class="dots"></span><span class="price">$ 4.50</span></div>
      <div class="row"><span>Scallop</span><span class="dots"></span><span class="price">$ 6.00</span></div>
      <div class="row"><span>Salad</span><span class="dots"></span><span class="price">$ 7.00</span></div>
      <div class="row"><span>Chip</span><span class="dots"></span><span class="price">$ 6.00</span></div>
      <div class="row"><span>Ham</span><span class="dots"></span><span class="price">$ 7.50</span></div>
      <div class="row"><span>Bacon</span><span class="dots"></span><span class="price">$ 7.00</span></div>
      <div class="row"><span>Chicken</span><span class="dots"></span><span class="price">$ 7.50</span></div>
      <div class="row"><span>Bacon/Egg</span><span class="dots"></span><span class="price">$ 7.00</span></div>
      <div class="row"><span>Roast Beef</span><span class="dots"></span><span class="price">$ 7.50</span></div>
      <div class="row"><span>Schnitzel</span><span class="dots"></span><span class="price">$ 8.50</span></div>
      <div class="row full"><span>Or create your own for $ &nbsp; Roll</span><span class="dots"></span><span class="price">+$ 6.00</span></div>
    </div>
  </section>
  <div class="art" role="img" aria-label="Line drawing of a sub sandwich" style="left:247px;top:17px;width:120px;height:48px"></div>

  <section class="section" style="left:16px;top:232px;width:372px">
    <h2>SALADS IN TUBS:</h2>
    <div class="rule" style="width:292px"></div>
    <div class="grid" style="grid-template-columns:172px 186px">
      <div class="row full"><span>Plain Salad</span><span class="dots"></span><span class="price">$ 7.50</span></div>
      <div class="row full"><span>Caesar Salad Tub</span><span class="dots"></span><span class="price">$ 10.00</span></div>
      <div class="row full"><span>Tomato/Beetroot/Onion/Cucumber</span><span class="dots"></span><span class="price">$ 0.50</span></div>
      <div class="row"><span>Bacon/ Meat</span><span class="dots"></span><span class="price">$ 2.50</span></div>
      <div class="row"><span>Pineapple</span><span class="dots"></span><span class="price">$ 1.00</span></div>
      <div class="row"><span>Egg</span><span class="dots"></span><span class="price">$ 1.50</span></div>
      <div class="row"><span>Sauce</span><span class="dots"></span><span class="price">$ 0.50</span></div>
      <div class="row full"><span>Kebab Meat: Chicken 100gr</span><span class="dots"></span><span class="price">$ 3.50</span></div>
      <div class="row"><span>Lamb 100gr</span><span class="dots"></span><span class="price">$ 4.50</span></div>
      <div class="row"><span>Avocado/ Cheese</span><span class="dots"></span><span class="price">$ 4.50</span></div>
    </div>
  </section>
  <div class="art" role="img" aria-label="Line drawing of a salad bowl" style="left:312px;top:226px;width:62px;height:38px"></div>

  <section class="section" style="left:16px;top:405px;width:372px">
    <h2>BURGERS: (BEEF OR CHICKEN)</h2>
    <div class="rule" style="width:358px;background:transparent;margin-bottom:11px"></div>
    <div class="grid" style="grid-template-columns:172px 186px">
      <div class="row"><span>Plain</span><span class="dots"></span><span class="price">$ 7.00</span></div>
      <div class="row"><span>Bacon/ Cheese</span><span class="dots"></span><span class="price">$ 9.00</span></div>
      <div class="row"><span>Works</span><span class="dots"></span><span class="price">$ 10.00</span></div>
      <div class="row"><span>Bacon/Egg Burger</span><span class="dots"></span><span class="price">$ 9.50</span></div>
      <div class="row"><span>Cheese</span><span class="dots"></span><span class="price">$ 8.00</span></div>
      <div class="row"><span>Mexican</span><span class="dots"></span><span class="price">$ 8.00</span></div>
      <div class="row full"><span>Schnitzel Burgers: Extra</span><span class="dots"></span><span class="price">$ 1.50</span></div>
      <div class="row full"><span>Hawaiian (Works burger with pineapple)</span><span class="dots"></span><span class="price">$ 11.00</span></div>
      <div class="text full">Mega (Works burger with double meat, double</div>
      <div class="row full"><span>Bacon and Egg)</span><span class="dots"></span><span class="price">$ 15.00</span></div>
    </div>
  </section>

  <section class="section" style="left:16px;top:564px;width:372px">
    <h2 class="tight">BACON/EGG ROLL OR WRAPS</h2>
    <div class="rule"></div>
    <div class="row"><span>Bacon/Egg</span><span class="dots"></span><span class="price">$ 7.00</span></div>
    <div class="row"><span>Bacon/Egg/Cheese</span><span class="dots"></span><span class="price">$ 8.20</span></div>
    <div class="row"><span>Bacon/Egg/Cheese/Onion</span><span class="dots"></span><span class="price">$ 9.20</span></div>
    <div class="row"><span>Wraps: Extra</span><span class="dots"></span><span class="price">$ 3.00</span></div>
  </section>
  <div class="art" role="img" aria-label="Illustration of a filled wrap" style="left:304px;top:555px;width:68px;height:28px;background:linear-gradient(90deg,#e8b64a,#8a7a2c)"></div>

  <section class="section" style="left:16px;top:671px;width:372px">
    <h2 class="tight">GRAVY ROLLS</h2>
    <div class="rule"></div>
    <div class="grid" style="grid-template-columns:172px 186px">
      <div class="row"><span>Slow Cook Beef</span><span class="dots"></span><span class="price">$ 8.50</span></div>
      <div class="row"><span>Sausage</span><span class="dots"></span><span class="price">$ 7.00</span></div>
      <div class="row"><span>Slow Cook Pork</span><span class="dots"></span><span class="price">$ 8.00</span></div>
      <div class="row"><span>Schnitzel</span><span class="dots"></span><span class="price">$ 8.00</span></div>
      <div class="row"><span>Rissole</span><span class="dots"></span><span class="price">$ 8.00</span></div>
      <div class="row"><span>Chips</span><span class="dots"></span><span class="price">$ 6.50</span></div>
    </div>
  </section>
  <div class="art" role="img" aria-label="Small illustration of a gravy roll" style="left:174px;top:670px;width:30px;height:24px;background:#c7703a"></div>

  <!-- Middle column -->
  <section class="section" style="left:412px;top:40px;width:362px">
    <h2>KEBABS</h2>
    <div class="rule" style="width:194px;margin-bottom:8px"></div>
    <div class="grid" style="grid-template-columns:172px 176px">
      <div class="row"><span>Chicken</span><span class="dots"></span><span class="price">$ 12.50</span></div>
      <div class="row" style="grid-row:span 2;align-items:center"><span>Lamb</span><span class="dots" style="transform:none"></span><span class="price">$ 14.50</span></div>
      <div class="row"><span>Mix</span><span class="dots"></span><span class="price">$ 14.50</span></div>
    </div>
  </section>
  <div class="art" role="img" aria-label="Line drawing of a kebab skewer" style="left:626px;top:42px;width:140px;height:28px"></div>

  <section class="section" style="left:412px;top:127px;width:362px">
    <h2 class="tight">SCHNITZEL WRAPS</h2>
    <div class="rule" style="width:282px"></div>
    <div class="row"><span>Caesar</span><span class="dots"></span><span class="price">$ 12.00</span></div>
    <div class="row"><span>Salad and Cheese</span><span class="dots"></span><span class="price">$ 11.00</span></div>
    <div class="text">Works (with bacon, egg, cheese and</div>
    <div class="row"><span>All salad):</span><span class="dots"></span><span class="price">$ 14.50</span></div>
    <div class="text" style="margin-top:3px">Mexican (Mexican spiced schnitzel with<br>lettuce, tomato, Spanish onion, cheese, sour</div>
    <div class="row"><span>cream and hot chilli sauce) :</span><span class="dots"></span><span class="price">$ 10.50</span></div>
    <div class="text" style="margin-top:3px">Hawaiian (with bacon, lettuce, tomato,</div>
    <div class="row"><span>pineapple, cheese with honey mustard)</span><span class="dots" style="border:0"></span><span class="price">$ 12.00</span></div>
  </section>
  <div class="art" role="img" aria-label="Illustration of a schnitzel wrap" style="left:677px;top:120px;width:42px;height:30px;background:linear-gradient(90deg,#e3c58a,#b66a3a)"></div>

  <section class="section" style="left:412px;top:343px;width:362px">
    <h2 class="tight">SNACK PACKS</h2>
    <div class="rule"></div>
    <div class="text note">(Kebab meats with chips, Spanish onions,<br>cheese and sauce of your choice)</div>
    <div style="width:172px;margin-top:6px">
      <div class="row"><span>Chips</span><span class="dots"></span><span class="price">$ 13.00</span></div>
      <div class="row"><span>Mix</span><span class="dots"></span><span class="price">$ 15.00</span></div>
      <div class="row"><span>Lamb</span><span class="dots"></span><span class="price">$ 15.00</span></div>
    </div>
  </section>

  <section class="section" style="left:412px;top:489px;width:362px">
    <h2>HOT FOOD</h2>
    <div class="rule" style="width:270px"></div>
    <div class="grid" style="grid-template-columns:172px 176px">
      <div class="row"><span>Scallop</span><span class="dots"></span><span class="price">$ 2.00</span></div>
      <div class="row"><span>Crunch Roll</span><span class="dots"></span><span class="price">$ 3.50</span></div>
      <div class="row"><span>Dim Sim</span><span class="dots"></span><span class="price">$ 2.00</span></div>
      <div class="row"><span>Battered Sav</span><span class="dots"></span><span class="price">$ 3.50</span></div>
      <div class="row"><span>Hash Brown</span><span class="dots"></span><span class="price">$ 2.50</span></div>
      <div class="row"><span>Dippy Dog</span><span class="dots"></span><span class="price">$ 4.50</span></div>
      <div class="row"><span>Sausage</span><span class="dots"></span><span class="price">$ 3.00</span></div>
      <div class="row"><span>Mini Chicken</span></div>
      <div class="row"><span>Corn Jack</span><span class="dots"></span><span class="price">$ 3.50</span></div>
      <div class="row"><span>Dim Sim *6</span><span class="dots"></span><span class="price">$ 3.00</span></div>
      <div class="row"><span>Chicken Stick</span><span class="dots"></span><span class="price">$ 3.70</span></div>
    </div>
  </section>
  <div class="art" role="img" aria-label="Line drawing of a steaming rice bowl" style="left:688px;top:475px;width:50px;height:46px"></div>

  <section class="section" style="left:412px;top:655px;width:362px">
    <h2 class="tight">CHIPS:</h2>
    <div class="rule"></div>
    <div class="row"><span>Small</span><span class="dots"></span><span class="price">$ 4.00</span></div>
    <div class="row"><span>Medium</span><span class="dots"></span><span class="price">$ 6.00</span></div>
    <div class="row"><span>Large</span><span class="dots"></span><span class="price">$ 8.00</span></div>
    <div class="row"><span>Add Gravy: Extra</span><span class="dots"></span><span class="price">$ 2.00</span></div>
  </section>
  <div class="art" role="img" aria-label="Illustration of a bowl of chips" style="left:574px;top:634px;width:62px;height:50px;background:linear-gradient(180deg,#e9d96a 0%,#e9d96a 55%,#d85a3a 56%)"></div>

  <!-- Right column -->
  <section class="section" style="left:794px;top:39px;width:355px">
    <h2 class="tight">BIG BREAKY (SPECIAL)</h2>
    <div class="rule" style="width:290px;margin-bottom:12px"></div>
    <div class="text" style="line-height:16px">Bacon, 2x eggs, sausage, fried tomato,</div>
    <div class="row" style="height:16px"><span>Hashbrown and toast</span><span class="dots"></span><span class="price">$ 15.00</span></div>
    <div class="row" style="height:16px"><span>With a small coffee</span><span class="dots"></span><span class="price">$ 17.00</span></div>
  </section>
  <div class="art" role="img" aria-label="Line drawing of a steaming coffee cup" style="left:1091px;top:31px;width:50px;height:54px"></div>

  <section class="section" style="left:794px;top:166px;width:355px">
    <h2>SEAFOOD</h2>
    <div class="rule" style="width:197px"></div>
    <div class="grid" style="grid-template-columns:128px 168px;column-gap:52px;width:348px">
      <div class="row"><span>Calamari Ring</span><span class="dots"></span><span class="price">$ 2.00</span></div>
      <div class="row"><span>Prawn Cutlet</span><span class="dots"></span><span class="price">$ 2.50</span></div>
      <div class="row"><span>Cocktail Fish</span><span class="dots"></span><span class="price">$ 2.50</span></div>
      <div class="row"><span>Fish Cake</span><span class="dots"></span><span class="price">$ 3.50</span></div>
      <div class="row"><span>Crab Stick</span><span class="dots"></span><span class="price">$ 2.50</span></div>
      <div class="row"><span>Battered Fish</span><span class="dots"></span><span class="price">$ 7.00</span></div>
    </div>
  </section>
  <div class="art" role="img" aria-label="Line drawing of a crab" style="left:998px;top:151px;width:55px;height:44px"></div>

  <section class="section" style="left:794px;top:276px;width:355px">
    <h2 class="tight">SEAFOOD PACK</h2>
    <div class="rule" style="margin-bottom:14px"></div>
    <div class="pack">
      <div class="row"><span><span class="note">#1:</span> Traditional: Battered fish &amp; chip:</span><span class="dots"></span><span class="price">$ 9.00</span></div>
    </div>
    <div class="pack">
      <div class="row"><span><span class="note">#2:</span> Snacking pack: 3 cocktail fish &amp; chip</span><span class="dots"></span><span class="price">$ 9.00</span></div>
    </div>
    <div class="pack">
      <div class="text"><span class="note">#3:</span> Fisherman basket (2 calamari ring, 2<br>prawn cutlet, 1 crabstick, 1 cocktail fish,</div>
      <div class="row"><span>chip &amp; 1 can of soft drink) :</span><span class="dots"></span><span class="price">$ 18.00</span></div>
    </div>
    <div class="pack">
      <div class="text"><span class="note">#4:</span> Family feast (4 prawn cutlets, 4<br>calamari rings, 4 crabstick, 6 cocktail fish &amp;</div>
      <div class="row"><span>1.25L bottle of soft drink) :</span><span class="dots"></span><span class="price">$ 40.00</span></div>
    </div>
  </section>
  <div class="art" role="img" aria-label="Line drawing of a fish on a plate with a glass of juice" style="left:860px;top:524px;width:193px;height:72px;border-radius:36px"></div>

</div>
</body>
</html>
```